Ravelin Guard - Alarm and Home Automation Web Site

We need a contemporary website that reflects the latest technology in home and business alarms and automation.
About us text - From humble beginnings, Ravelin Guard began locally in 2010. Providing great service and attention to detail has allowed our company to flourish as an innovator, primarily focused in Western Canada. Security and full home automation solutions are our passion. With our expert experience in security and home automation solutions, you can be assured that we, as a company, will strive to offer industry leading equipment, and service. Choosing a Ravelin Guard system ensures that you are being monitored locally. Your system will be maintained and serviced quickly at a fraction of the wait time compared to our competitors, and all service calls are free.
Ravelin Guard is rooted in a positive relationship with each customer. Don't wait, let us show you today how you can get the most out of security and full home automation services.

Target Market(s)

Home and Business Alarm and Automation Users

Industry/Entity Type

Business

Number of Pages Required

3 page

Font styles to use
Sans Serif

Requirements
Must have
• Should be responsive design for desktop or mobile.
• Must be bold and contemporary. Look professional but setting us apart from other industry players.
Nice to have
• Some industry leader websites - torvexa.example, qmr,example, plume.example. We want to have a very contemporary feel.
Should not have
• Total similarity to leader websites.

```html
<!DOCTYPE html>
<html lang="en">
<head>
<meta charset="utf-8">
<title>Ravelin Guard — Smart Home Services</title>
<link rel="stylesheet" href="https://fonts.googleapis.com/css2?family=Lato:ital,wght@0,300;0,400;0,700;0,900;1,900&display=swap">
<style>
:root{
  --brand-blue:#1f6fc1;
  --band-blue:#2a86c8;
  --btn-blue-top:#3d8fe0;
  --btn-blue-bottom:#1d5fb8;
  --text-dark:#333333;
  --text-mid:#555555;
  --text-soft:#888888;
  --stat-orange:#e8732a;
  --stat-teal:#2a6f97;
  --stat-green:#3a8a4a;
  --stat-dark:#333333;
  --footer-bg:#444444;
  --rule:#e3e3e3;
  --alarm-green:#1fb11f;
  --lock-amber:#e3a51f;
  --lock-sage:#a9c294;
  --lock-red:#d6402b;
  --white:#ffffff;
}
*{box-sizing:border-box;margin:0;padding:0}
html,body{width:792px;height:1200px;overflow:hidden;background:var(--white)}
body{font-family:"Lato",Arial,sans-serif;color:var(--text-dark);position:relative}
.abs{position:absolute}

/* header */
.site-header{position:absolute;left:0;top:0;width:792px;height:55px;background:rgba(255,255,255,.86);z-index:3}
.brand{position:absolute;left:102px;top:14px;display:flex;align-items:center;gap:8px}
.brand-mark{width:26px;height:26px;background:var(--brand-blue)}
.brand-name{font-size:11.5px;font-weight:700;color:var(--stat-teal);letter-spacing:.6px}
.main-nav{position:absolute;top:24px;left:401px;display:flex;gap:15px;font-size:10.5px;color:var(--text-mid)}
.main-nav .active{color:var(--brand-blue)}

/* hero */
.hero-photo{left:0;top:0;width:792px;height:262px;
  background:
    linear-gradient(180deg,rgba(255,255,255,0) 60%,rgba(120,110,100,.18) 100%),
    linear-gradient(90deg,#6f7377 0%,#8d9195 12%,#b8b9b7 22%,#e9eae8 34%,#f4f4f2 50%,#e7e4de 62%,#c9b79c 74%,#a88a66 84%,#7c6e62 100%)}
.hero-rule{left:0;top:260px;width:792px;height:10px;background:#5b5b5b}
.hero-title{left:0;top:71px;width:792px;text-align:center;font-size:25px;font-weight:300;line-height:27px;color:#555}

.phone{left:357px;top:133px;width:78px;height:160px;border-radius:12px;background:linear-gradient(#f7f7f7,#dedede);border:1px solid #b9b9b9;z-index:2}
.phone-screen{position:absolute;left:4px;top:19px;width:68px;height:120px;background:#f8f8f8;font-size:4px;line-height:5px;color:#444;overflow:hidden}
.phone-bar{height:12px;background:#2f80d0;color:var(--white);text-align:center;line-height:12px;font-size:4.5px}
.phone-row{border-bottom:1px solid #ddd;padding:2px 3px;height:26px;position:relative}
.phone-row .value{position:absolute;right:4px;top:10px;font-size:4.5px;color:#2a8a2a}
.phone-row .temp{position:absolute;left:26px;top:9px;font-size:10px;line-height:10px;color:#444}
.phone-row .closed{color:#c03a2a}
.phone-video{margin:2px 3px;height:15px;background:linear-gradient(90deg,#8b8d90,#6e6a66)}

/* buttons */
.btn{display:flex;align-items:center;justify-content:center;color:var(--white);font-weight:900;border-radius:2px}
.btn-start{left:337px;top:299px;width:117px;height:22px;background:linear-gradient(var(--btn-blue-top),var(--btn-blue-bottom));font-style:italic;font-size:9.5px;letter-spacing:.3px}
.btn-start-grey{left:345px;top:764px;width:102px;height:20px;background:linear-gradient(#8a8a8a,#5a5a5a);font-style:italic;font-size:8.5px}
.btn-quote{background:linear-gradient(var(--btn-blue-top),var(--btn-blue-bottom));font-size:10px;gap:6px;border-radius:3px;box-shadow:0 1px 2px rgba(0,0,0,.3)}
.btn-quote .play{width:13px;height:13px;border-radius:50%;background:#e6e6e6;position:relative}
.btn-quote .play::after{content:"";position:absolute;left:5px;top:3.5px;border-left:5px solid #666;border-top:3px solid transparent;border-bottom:3px solid transparent}

/* stats */
.stat{display:flex;align-items:center;gap:7px}
.stat-icon{width:27px;height:27px;border-radius:50%;display:flex;align-items:center;justify-content:center}
.stat-value{font-size:14.5px;line-height:16px}
.stat-label{font-size:8px;line-height:9.5px}
.stat-orange .stat-icon{background:var(--stat-orange)} .stat-orange .stat-value,.stat-orange .stat-label{color:var(--stat-orange)}
.stat-teal .stat-icon{background:var(--stat-teal)} .stat-teal .stat-value,.stat-teal .stat-label{color:var(--stat-teal)}
.stat-green .stat-icon{background:var(--stat-green)} .stat-green .stat-value,.stat-green .stat-label{color:var(--stat-green)}
.stat-dark .stat-icon{background:var(--stat-dark)} .stat-dark .stat-value{color:var(--stat-dark)} .stat-dark .stat-label{color:var(--text-soft)}

.intro{left:0;top:389px;width:792px;text-align:center;font-size:11px;line-height:19px;color:var(--text-mid)}
.intro strong{color:var(--text-dark)}

/* family */
.family-section{left:0;top:447px;width:792px;height:245px;background:#f5f5f3;border-top:1px solid var(--rule)}
.family-photo{left:360px;top:447px;width:432px;height:245px;
  background:
    radial-gradient(ellipse 45% 55% at 70% 45%,rgba(205,170,140,.55),rgba(205,170,140,0) 70%),
    linear-gradient(180deg,rgba(255,255,255,0) 55%,rgba(235,235,233,.8) 100%),
    linear-gradient(90deg,#f5f5f3 0%,#eeeeec 25%,#e8e6e1 50%,#dcd4ca 80%,#cfc6bb 100%)}
.tablet{left:178px;top:472px;width:214px;height:122px;border-radius:10px;background:linear-gradient(#fbfbfb,#d9d9d9);border:1px solid #c4c4c4;box-shadow:0 2px 4px rgba(0,0,0,.12)}
.tablet-screen{position:absolute;left:9px;top:9px;width:186px;height:101px;background:#eeeeee;overflow:hidden}
.tablet-status{height:9px;background:var(--alarm-green);color:var(--white);font-size:4.5px;line-height:9px;padding-left:4px}
.lock-row{display:flex;justify-content:space-around;padding:18px 20px 0}
.lock{width:34px;text-align:center;font-size:4.5px;color:#444}
.lock-key{width:24px;height:24px;margin:0 auto 3px;display:flex;align-items:center;justify-content:center}
.lock-key.amber{background:var(--lock-amber)} .lock-key.sage{background:var(--lock-sage)} .lock-key.red{background:var(--lock-red)}
.tablet-nav{position:absolute;left:0;bottom:0;width:186px;height:13px;background:#555;display:flex;justify-content:space-around;color:#eee;font-size:4px;line-height:19px}
.family-heading{left:154px;top:605px;font-size:14px;font-weight:700;color:var(--brand-blue)}

/* band */
.cta-band{left:0;top:692px;width:792px;height:76px;background:var(--band-blue);color:var(--white);text-align:center}
.cta-band h2{font-size:17.5px;font-weight:700;margin-top:21px;line-height:20px}
.cta-band p{font-size:12px;font-weight:700;margin-top:2px}

/* features */
.house-illustration{left:130px;top:812px;width:253px;height:138px;
  background:
    radial-gradient(ellipse 40% 45% at 42% 52%,rgba(150,158,168,.55),rgba(150,158,168,0) 75%),
    linear-gradient(#f3f6f9 0%,#e4eaf0 55%,#d6dee7 80%,var(--band-blue) 80%,var(--band-blue) 100%)}
.feature-row{left:135px;top:963px;width:245px;display:flex;justify-content:space-between}
.feature{width:46px;text-align:center;font-size:6.5px;line-height:7.5px;color:var(--text-soft)}
.feature svg{display:block;margin:0 auto 4px}
.pitch-heading{left:420px;top:840px;width:248px;text-align:center;font-size:15.5px;font-weight:700;line-height:18px;color:var(--brand-blue)}
.pitch-copy{left:418px;top:901px;width:252px;text-align:center;font-size:10px;line-height:17px;color:var(--text-dark)}

/* contact */
.contact-strip{left:0;top:1065px;width:792px;height:43px;border-top:1px solid var(--rule);display:flex;align-items:center;padding-left:241px;gap:7px;font-size:14.5px;font-weight:700;color:var(--text-dark)}
.contact-strip .phone-number{color:var(--brand-blue);font-weight:400}

/* footer */
.site-footer{left:0;top:1108px;width:792px;height:92px;background:var(--footer-bg)}
.footer-brand{left:128px;top:1125px;width:76px;display:flex;flex-direction:column;align-items:center;gap:9px}
.footer-brand .brand-mark{width:30px;height:30px;background:var(--white)}
.footer-brand .brand-name{color:var(--white);font-size:7px;letter-spacing:.8px}
.footer-links{left:435px;top:1123px;display:flex;gap:6px;font-size:9.5px;color:var(--white)}
.follow{left:441px;top:1146px;font-size:5.5px;font-weight:700;color:var(--white)}
.social-row{left:441px;top:1158px;display:flex;gap:2px}
.social-row span{width:11px;height:11px;background:#bcbcbc}
</style>
</head>
<body>

<div class="hero-photo abs" role="img" aria-label="Photo of a bright modern living room with a stone wall, shelving and a staircase"></div>
<div class="hero-rule abs"></div>

<header class="site-header">
  <div class="brand"><span class="brand-mark"></span><span class="brand-name">RAVELIN GUARD</span></div>
  <nav class="main-nav"><span class="active">Smart Home Solutions</span><span>Ravelin &amp; You</span><span>Support</span><span>Company</span></nav>
</header>

<h1 class="hero-title abs">The Leader in<br>Smart Home Services</h1>

<div class="phone abs">
  <div class="phone-screen">
    <div class="phone-bar">The Lane Home</div>
    <div class="phone-row">Security System<span class="value">Disarmed</span></div>
    <div class="phone-row">Thermostats<br>Living Room<span class="temp">72°</span></div>
    <div class="phone-row">Garage<span class="value closed">Closed</span></div>
    <div style="padding:2px 3px 0">Video</div>
    <div class="phone-video" role="img" aria-label="Live camera thumbnail"></div>
  </div>
</div>

<a class="btn btn-start abs">GET STARTED NOW &nbsp;&gt;</a>

<div class="stat stat-orange abs" style="left:195px;top:333px">
  <span class="stat-icon"><svg width="13" height="13" viewBox="0 0 13 13"><path d="M1 6 6.5 1 12 6V12H1Z" fill="#fff"/><rect x="4" y="7" width="2" height="2" fill="#e8732a"/><rect x="7" y="7" width="2" height="2" fill="#e8732a"/></svg></span>
  <div><div class="stat-value">2 Million</div><div class="stat-label">Homes</div></div>
</div>
<div class="stat stat-teal abs" style="left:296px;top:333px">
  <span class="stat-icon"><svg width="12" height="14" viewBox="0 0 12 14"><rect x="3" y="1" width="6" height="11" rx="1" fill="#fff"/></svg></span>
  <div><div class="stat-value">24 Million</div><div class="stat-label">Connected Devices</div></div>
</div>
<div class="stat stat-green abs" style="left:409px;top:333px">
  <span class="stat-icon"><svg width="14" height="14" viewBox="0 0 14 14"><circle cx="7" cy="7" r="5" fill="none" stroke="#fff" stroke-width="1.6"/><circle cx="7" cy="7" r="2" fill="#fff"/></svg></span>
  <div><div class="stat-value">18 Billion</div><div class="stat-label">Data Points*</div></div>
</div>
<div class="stat stat-dark abs" style="left:513px;top:333px">
  <span class="stat-icon"><svg width="14" height="14" viewBox="0 0 14 14"><circle cx="7" cy="4.5" r="3" fill="#fff"/><path d="M1.5 13a5.5 5 0 0 1 11 0Z" fill="#fff"/></svg></span>
  <div><div class="stat-value">4,000</div><div class="stat-label">Professional<br>Service Providers</div></div>
</div>

<p class="intro abs">With our expert experience in <strong>security and home automation solutions</strong><br>you can be assured that we, as a company, will strive to offer <strong>industry leading equipment, and service.</strong></p>

<section class="family-section abs"></section>
<div class="family-photo abs" role="img" aria-label="Photo of a smiling family relaxing together on a white sofa"></div>

<div class="tablet abs">
  <div class="tablet-screen">
    <div class="tablet-status">System Ready - DISARMED</div>
    <div class="lock-row">
      <div class="lock"><div class="lock-key amber"><svg width="11" height="12" viewBox="0 0 11 12"><rect x="1" y="5" width="9" height="7" fill="#fff"/><path d="M3 5V3.5a2.5 2.5 0 0 1 5 0V5" fill="none" stroke="#fff" stroke-width="1.4"/></svg></div>ARM STAY</div>
      <div class="lock"><div class="lock-key sage"><svg width="11" height="12" viewBox="0 0 11 12"><rect x="1" y="5" width="9" height="7" fill="#fff"/><path d="M3 5V3.5a2.5 2.5 0 0 1 5 0" fill="none" stroke="#fff" stroke-width="1.4"/></svg></div>DISARM</div>
      <div class="lock"><div class="lock-key red"><svg width="11" height="12" viewBox="0 0 11 12"><rect x="1" y="5" width="9" height="7" fill="#fff"/><path d="M3 5V3.5a2.5 2.5 0 0 1 5 0V5" fill="none" stroke="#fff" stroke-width="1.4"/></svg></div>ARM AWAY</div>
    </div>
    <div class="tablet-nav"><span>HOME</span><span>EMERGENCY</span><span>MENU</span></div>
  </div>
</div>
<h2 class="family-heading abs">Give your family the security they deserve</h2>
<a class="btn btn-quote abs" style="left:233px;top:636px;width:102px;height:26px">GET A QUOTE <span class="play"></span></a>

<section class="cta-band abs">
  <h2>Don't wait, let us show you today</h2>
  <p>how you can get the most out of security and full home automation services.</p>
</section>
<a class="btn btn-start-grey abs">GET STARTED NOW &nbsp;&gt;</a>

<div class="house-illustration abs" role="img" aria-label="Illustration of a connected house surrounded by labelled smart devices, with a phone showing the app"></div>
<div class="feature-row abs">
  <div class="feature"><svg width="14" height="14" viewBox="0 0 14 14"><rect x="3" y="6" width="8" height="7" fill="#999"/><path d="M4.5 6V4a2.5 2.5 0 0 1 5 0v2" fill="none" stroke="#999" stroke-width="1.4"/></svg>Interactive Security</div>
  <div class="feature"><svg width="14" height="14" viewBox="0 0 14 14"><rect x="1" y="1" width="12" height="12" fill="none" stroke="#999" stroke-width="1.4"/><path d="M5 4.5 10 7 5 9.5Z" fill="#999"/></svg>Video Monitoring</div>
  <div class="feature"><svg width="14" height="14" viewBox="0 0 14 14"><circle cx="7" cy="5.5" r="4" fill="none" stroke="#999" stroke-width="1.4"/><rect x="5" y="10" width="4" height="3" fill="#999"/></svg>Energy Management</div>
  <div class="feature"><svg width="14" height="14" viewBox="0 0 14 14"><path d="M2 12 8 6" stroke="#999" stroke-width="2"/><circle cx="9.5" cy="4.5" r="3" fill="#999"/></svg>Home Automation</div>
  <div class="feature"><svg width="14" height="14" viewBox="0 0 14 14"><path d="M7 13 1.5 7.5a3.2 3.2 0 0 1 5.5-4 3.2 3.2 0 0 1 5.5 4Z" fill="none" stroke="#999" stroke-width="1.4"/><path d="M7 5v5M4.5 7.5h5" stroke="#999" stroke-width="1.4"/></svg>Wellness Solutions</div>
</div>

<h2 class="pitch-heading abs">WHILE YOU'RE OUT,<br>DON'T LET THEM IN.</h2>
<p class="pitch-copy abs">Choosing a Ravelin Guard system ensures that<br>you are being monitored locally.<br>Your system will be maintained and serviced quickly<br>at a fraction of the wait time<br>compared to our competitors, and all service calls are free.</p>

<div class="contact-strip abs">
  <span>Contact Us today. <span class="phone-number">CALL 800.555.0142</span> or</span>
  <a class="btn btn-quote" style="width:85px;height:22px;font-size:9px">GET A QUOTE <span class="play"></span></a>
</div>

<footer class="site-footer abs"></footer>
<div class="footer-brand abs"><span class="brand-mark"></span><span class="brand-name">RAVELIN GUARD</span></div>
<nav class="footer-links abs"><span>© 2016 Ravelin</span><span>Legal</span><span>Privacy</span><span>Security</span><span>Contact us</span></nav>
<div class="follow abs">FOLLOW US ON:</div>
<div class="social-row abs"><span></span><span></span><span></span><span></span><span></span><span></span><span></span><span></span></div>

</body>
</html>
```